" Montamos roteiros turisticos especializados em experiência. Inicialmente a empresa ofertará roteiros especializados para fotografia, porém no futuro poderá conter roteiros para vinhos, culinária, esportes, etc. "

```html
<!DOCTYPE html>
<html lang="pt-BR">
<head>
<meta charset="UTF-8">
<title>Roteira — Roteiros de Experiência</title>
<link rel="stylesheet" href="https://fonts.googleapis.com/css2?family=Montserrat:wght@400;500;600;700;800&display=swap">
<style>
  :root {
    --page-bg: #e6e7ea;
    --header-bg: #131820;
    --hero-dark: #1d2320;
    --hero-mid: #3c4640;
    --hero-warm: #6a5a44;
    --text-light: #f3f4f2;
    --text-muted: #b9bfbb;
    --accent: #2ec48e;
    --panel-bg: #ffffff;
    --panel-line: #d9dcdf;
    --panel-text: #3a3f44;
  }
  * { box-sizing: border-box; margin: 0; padding: 0; }
  html, body {
    width: 1200px; height: 1200px; overflow: hidden;
    background: var(--page-bg);
    font-family: "Montserrat", sans-serif;
  }
  .site {
    position: absolute; left: 0; top: 220px;
    width: 1200px; height: 760px;
    background: var(--hero-dark);
    overflow: hidden;
  }
  .site-header {
    position: absolute; left: 0; top: 0; width: 100%; height: 64px;
    background: var(--header-bg);
    display: flex; align-items: center;
    padding: 0 48px;
    z-index: 2;
  }
  .brand {
    display: flex; align-items: center; gap: 8px;
    color: var(--text-light);
    font-weight: 700; font-size: 26px; letter-spacing: -0.5px;
  }
  .brand-dot { width: 9px; height: 9px; border-radius: 50%; background: var(--accent); }
  .main-nav { display: flex; gap: 30px; margin-left: 170px; }
  .main-nav a {
    color: var(--text-light); text-decoration: none;
    font-size: 11px; font-weight: 600; letter-spacing: 1px;
  }
  .header-tools { margin-left: auto; display: flex; align-items: center; gap: 26px; }
  .social { display: flex; gap: 10px; }
  .social span { width: 12px; height: 12px; border-radius: 50%; background: var(--text-muted); }
  .lang { display: flex; gap: 8px; font-size: 10px; font-weight: 600; color: var(--text-muted); }
  .lang .active { color: var(--accent); }
  .hero-photo {
    position: absolute; inset: 64px 0 0 0;
    background:
      radial-gradient(ellipse at 70% 25%, rgba(210,200,170,0.35), transparent 55%),
      linear-gradient(180deg, #4d5850 0%, var(--hero-mid) 40%, #2a302c 62%, var(--hero-warm) 78%, #2b241c 100%);
  }
  .hero-shade {
    position: absolute; inset: 64px 0 0 0;
    background: linear-gradient(90deg, rgba(10,12,12,0.55) 0%, rgba(10,12,12,0.15) 60%, rgba(10,12,12,0.05) 100%);
  }
  .hero-content { position: absolute; left: 110px; top: 300px; z-index: 2; }
  .hero-title {
    color: var(--text-light); font-weight: 600; font-size: 40px; letter-spacing: 1px;
  }
  .hero-subtitle {
    margin-top: 6px; color: var(--text-muted);
    font-size: 12px; font-weight: 500; letter-spacing: 3px;
  }
  .hero-cta { margin-top: 60px; display: flex; align-items: center; gap: 14px; }
  .play-button {
    width: 42px; height: 42px; border-radius: 50%;
    border: 2px solid var(--text-light);
    display: flex; align-items: center; justify-content: center;
  }
  .cta-label { color: var(--text-light); font-size: 11px; font-weight: 600; letter-spacing: 1.5px; line-height: 1.4; }
  .slider-dots { position: absolute; left: 110px; bottom: 60px; display: flex; gap: 8px; z-index: 2; }
  .slider-dots span { width: 8px; height: 8px; border-radius: 50%; background: var(--text-muted); }
  .slider-dots .active { background: var(--text-light); width: 22px; border-radius: 4px; }
  .chat-panel {
    position: absolute; right: 90px; top: 470px; width: 230px; z-index: 2;
    background: var(--panel-bg); border-radius: 4px;
    box-shadow: 0 6px 18px rgba(0,0,0,0.3);
    font-size: 11px; color: var(--panel-text);
  }
  .chat-title { padding: 10px 12px; font-weight: 700; border-bottom: 1px solid var(--panel-line); }
  .chat-body { padding: 12px; height: 78px; }
  .chat-input { margin: 0 12px 12px; height: 26px; border: 1px solid var(--panel-line); border-radius: 3px; }
  .chat-toggle {
    position: absolute; right: 90px; top: 665px; z-index: 2;
    width: 30px; height: 30px; border-radius: 4px; background: var(--panel-bg);
  }
</style>
</head>
<body>
  <main class="site">
    <header class="site-header">
      <div class="brand"><span>Roteira</span><span class="brand-dot"></span></div>
      <nav class="main-nav">
        <a href="#">HOME</a>
        <a href="#">QUEM SOMOS</a>
        <a href="#">ROTEIROS</a>
        <a href="#">CONTATO</a>
        <a href="#">EXPERIÊNCIAS</a>
      </nav>
      <div class="header-tools">
        <div class="social"><span></span><span></span></div>
        <div class="lang"><span class="active">PT</span><span>EN</span></div>
        <svg width="16" height="16" viewBox="0 0 16 16" aria-label="Buscar">
          <circle cx="6.5" cy="6.5" r="5" fill="none" stroke="#f3f4f2" stroke-width="1.8"/>
          <line x1="10.2" y1="10.2" x2="15" y2="15" stroke="#f3f4f2" stroke-width="1.8"/>
        </svg>
      </div>
    </header>

    <div class="hero-photo" role="img" aria-label="Fotografia de uma câmera e um tripé sobre mesa de madeira, com montanhas e névoa ao fundo"></div>
    <div class="hero-shade"></div>

    <section class="hero-content">
      <h1 class="hero-title">UMA EXPERIÊNCIA INEXPLICÁVEL</h1>
      <p class="hero-subtitle">ALÉM DOS SEUS LIMITES</p>
      <div class="hero-cta">
        <div class="play-button">
          <svg width="14" height="14" viewBox="0 0 14 14"><polygon points="3,1 13,7 3,13" fill="#f3f4f2"/></svg>
        </div>
        <div class="cta-label">VEJA<br>O QUE FAZEMOS</div>
      </div>
    </section>

    <div class="slider-dots"><span class="active"></span><span></span><span></span><span></span></div>

    <aside class="chat-panel">
      <div class="chat-title">Fale conosco</div>
      <div class="chat-body">Olá! Como podemos ajudar?</div>
      <div class="chat-input"></div>
    </aside>
    <div class="chat-toggle"></div>
  </main>
</body>
</html>
```